web site update

I want to get a better website for a small high end remodeling and construction company
I currently have a web site but you will find that it is not good.
www.quenbrickhall.com
We are a high end construction / remodeling company that has been in business since 2003. We primarily work in the mid peninsula of the bay area. Most of our clientele are very educated captains of industry. This group is still the target client.
I had my logo designed by Mint Easel a few years ago and I do like it, I like the orange and black or orange a blue. I don’t have a lot of content on hand as far as professional photographs.
Number of pages not sure and are open to: design pages vs full function website
I think what I am after is a web presence that will seal the deal as we are getting high referrals from past clients.
Construction
1 page

```html
<!DOCTYPE html>
<html lang="en">
<head>
<meta charset="utf-8">
<title>Quenbrick Hall Remodeling</title>
<link href="https://fonts.googleapis.com/css2?family=Roboto:ital,wght@0,300;0,400;0,500;0,700;1,700&family=Montserrat:wght@400;500&display=swap" rel="stylesheet">
<style>
:root{
  --orange:#f26b0f;
  --orange-band:#e8721c;
  --ink:#1c1c1c;
  --text:#444;
  --muted:#777;
  --white:#fff;
  --light:#efefef;
  --footer:#363636;
  --base:#141414;
  --hero-dark:#2b2520;
}
*{box-sizing:border-box;margin:0;padding:0}
html,body{width:1200px;height:2985px;overflow:hidden}
body{font-family:"Montserrat",sans-serif;color:var(--text);background:var(--white);position:relative}
.head-font{font-family:"Roboto",sans-serif}
section,header,footer{position:absolute;left:0;width:1200px}
.accent{color:var(--orange)}
p{line-height:1.75}

/* header */
.site-header{top:0;height:105px;background:var(--white);border-bottom:1px solid #ddd}
.brand{position:absolute;left:102px;top:26px;display:flex;align-items:center;gap:12px}
.brand-mark{width:30px;height:30px;background:var(--orange)}
.brand-name{font-family:"Roboto",sans-serif;font-weight:700;font-size:22px;color:var(--ink);letter-spacing:1px;text-transform:uppercase}
.call{position:absolute;right:96px;top:10px;text-align:right}
.call-number{font-family:"Roboto",sans-serif;font-size:26px;font-weight:500;color:var(--ink);display:flex;align-items:center;justify-content:flex-end;gap:10px}
.call-address{font-size:10px;color:var(--muted);margin-top:4px}
.main-nav{position:absolute;right:96px;top:78px;display:flex;gap:44px;font-family:"Roboto",sans-serif;font-size:12px;font-weight:500;color:var(--ink);text-transform:uppercase}
.main-nav .current{color:var(--orange)}

/* hero */
.hero{top:105px;height:517px;border-bottom:4px solid var(--orange)}
.hero-photo{position:absolute;inset:0;background:linear-gradient(180deg,#3a322b 0%,#2a2420 45%,#3b3029 75%,#4a3a2c 100%)}
.hero-content{position:absolute;left:0;right:0;top:88px;text-align:center;color:var(--white)}
.hero-title{font-family:"Roboto",sans-serif;font-weight:300;font-size:82px;line-height:1;letter-spacing:1px}
.hero-title b{font-weight:400}
.hero-sub{font-family:"Roboto",sans-serif;font-weight:500;font-size:20px;margin-top:18px;text-transform:uppercase}
.hero-text{width:960px;margin:26px auto 0;font-size:16px;line-height:1.7}
.btn-ghost{display:inline-block;margin-top:40px;width:234px;height:52px;line-height:50px;border:1px solid rgba(255,255,255,.7);border-radius:26px;background:rgba(255,255,255,.08);font-family:"Roboto",sans-serif;font-size:13px;font-weight:500;text-transform:uppercase}

/* about */
.about{top:626px;height:400px;background:var(--white)}
.section-heading{font-family:"Roboto",sans-serif;font-weight:500;font-size:38px;color:var(--ink);text-transform:uppercase}
.about .section-heading{position:absolute;left:100px;top:38px}
.about-text{position:absolute;left:100px;top:100px;width:536px;font-size:10.5px;color:#555}
.read-more-link{position:absolute;left:100px;top:290px;font-size:12px;color:var(--orange)}
.video{position:absolute;left:672px;top:46px;width:430px;height:300px;background:linear-gradient(135deg,#3c3426 0%,#1e1b16 60%,#2c2a25 100%)}
.play{position:absolute;left:194px;top:130px}

/* services */
.services{top:1026px;height:625px}
.services-photo{position:absolute;inset:0;background:linear-gradient(180deg,#221c17 0%,#2e241c 50%,#3a2e24 100%)}
.services-inner{position:absolute;inset:0;color:var(--white);text-align:center}
.services .section-heading{color:var(--white);margin-top:42px}
.tagline{font-size:9px;color:#bbb;letter-spacing:1px;margin-top:4px;text-transform:uppercase}
.service{position:absolute;top:142px;width:310px;text-align:center}
.service-frame{position:relative;height:198px;padding:12px 18px}
.service-image{width:100%;height:100%}
.corner{position:absolute;width:24px;height:24px;border-color:var(--orange);border-style:solid}
.corner.tl{left:0;top:0;border-width:5px 0 0 5px}
.corner.tr{right:0;top:0;border-width:5px 5px 0 0}
.corner.bl{left:0;bottom:0;border-width:0 0 5px 5px}
.corner.br{right:0;bottom:0;border-width:0 5px 5px 0}
.service-title{font-family:"Roboto",sans-serif;font-weight:700;font-size:19px;color:var(--orange);margin-top:18px;text-transform:uppercase}
.service-text{font-size:10.5px;line-height:1.8;margin:8px 14px 0}
.service-more{font-size:10px;font-weight:500;margin-top:12px;text-transform:uppercase}
.btn-light{position:absolute;left:400px;top:520px;width:400px;height:52px;line-height:52px;border-radius:26px;background:var(--white);color:var(--orange);font-family:"Roboto",sans-serif;font-weight:700;font-size:12.5px;text-transform:uppercase}

/* blog */
.blog{top:1651px;height:524px;background:var(--light);text-align:center}
.blog .section-heading{margin-top:44px}
.post{position:absolute;top:122px;width:318px;height:352px;background:var(--white);border:1px solid #d9d9d9;padding:9px;text-align:left}
.post-image{height:190px}
.post-title{font-family:"Roboto",sans-serif;font-weight:500;font-size:19px;color:var(--orange);margin-top:14px;text-transform:uppercase}
.post-meta{display:flex;gap:30px;font-size:10px;color:#999;margin-top:6px;align-items:center}
.post-meta span{display:flex;align-items:center;gap:6px}
.post-text{font-size:10.5px;color:#555;margin-top:8px}

/* testimonial */
.testimonial{top:2175px;height:285px;background:var(--orange-band);text-align:center;color:var(--white)}
.quote-icon{margin-top:100px}
.quote-text{width:760px;margin:8px auto 0;font-family:"Roboto",sans-serif;font-style:italic;font-weight:700;font-size:11.5px;line-height:2}
.quote-name{font-family:"Roboto",sans-serif;font-style:italic;font-weight:700;font-size:12px;color:var(--ink);margin-top:8px;line-height:1.4}

/* footer */
.site-footer{top:2460px;height:390px;background:var(--footer);color:var(--white)}
.contacts{position:absolute;top:50px;left:98px;right:98px;height:50px}
.contact{position:absolute;display:flex;align-items:center;gap:16px;font-size:13px;line-height:1.55}
.icon-ring{width:46px;height:46px;border:2px solid var(--white);border-radius:50%;display:flex;align-items:center;justify-content:center;flex:none}
.newsletter{position:absolute;left:0;right:0;top:140px;text-align:center}
.newsletter .section-heading{color:var(--white);font-weight:400;font-size:30px}
.newsletter p{width:880px;margin:10px auto 0;font-size:10.5px;color:#999;line-height:2.3}
.subscribe{position:absolute;left:268px;top:278px;display:flex;gap:14px}
.subscribe-field{width:506px;height:46px;background:var(--white);color:#999;font-size:12px;padding:15px 8px}
.subscribe-btn{width:144px;height:46px;background:var(--orange);color:var(--white);font-family:"Roboto",sans-serif;font-weight:500;font-size:15px;line-height:46px;text-align:center;text-transform:uppercase}

.base-bar{top:2850px;height:135px;background:var(--base);text-align:center}
.base-nav{display:flex;justify-content:center;gap:60px;margin-top:34px;font-size:11px;color:#3a3a3a;text-transform:uppercase}
.base-nav .current{color:var(--orange)}
.copyright{font-size:10px;color:#3a3a3a;margin-top:36px}
</style>
</head>
<body>

<header class="site-header">
  <div class="brand">
    <span class="brand-mark"></span>
    <span class="brand-name">Quenbrick Hall Remodeling</span>
  </div>
  <div class="call">
    <div class="call-number">
      <svg width="24" height="24" viewBox="0 0 24 24"><rect x="3" y="3" width="18" height="18" transform="rotate(45 12 12)" fill="#f26b0f"/><path d="M9 8c.6-.5 1.2-.3 1.5.3l.7 1.3c.3.5.1 1-.3 1.3l-.4.3c.5 1.1 1.2 1.9 2.3 2.4l.3-.4c.3-.4.9-.5 1.3-.2l1.2.7c.6.4.7 1 .2 1.5-1 1-2.4 1-3.8 0-1.7-1.2-3-2.6-3.6-4.3-.4-1.2-.3-2.1.6-2.9z" fill="#fff"/></svg>
      415.555.0148
    </div>
    <div class="call-address">2140 - 2146 Alder Lane, Redwood Point, CA 94061</div>
  </div>
  <nav class="main-nav">
    <span class="current">Home</span><span>About</span><span>Services</span><span>Gallery</span><span>Contact Us</span>
  </nav>
</header>

<section class="hero">
  <div class="hero-photo" role="img" aria-label="Photo of a dim remodeled interior with a glass dining table and windows"></div>
  <div class="hero-content">
    <h1 class="hero-title"><span>13</span> <b>YEARS</b></h1>
    <div class="hero-sub">Of experience in the industry</div>
    <p class="hero-text">Lorem ipsum dolor sit amet, consectetuer adipiscing elit, sed diam nonummy nibh euismod tincidunt ut laoreet dolore magna aliquam erat volutpat. Ut wisi enim ad minim veniam, quis nostrud exerci tation</p>
    <span class="btn-ghost">See More</span>
  </div>
</section>

<section class="about">
  <h2 class="section-heading">About <span class="accent">Us</span></h2>
  <p class="about-text">Lorem ipsum dolor sit amet, consectetuer adipiscing elit, sed diam nonummy nibh euismod tincidunt ut laoreet dolore magna aliquam erat volutpat. Ut wisi enim ad minim veniam, quis nostrud exercitation ullamcorper suscipit lobortis nisl ut aliquip ex ea commodo consequat. Duis autem vel eum iriure dolor in hendrerit in vulputate velit esse molestie consequat, vel illum dolore eu feugiat nulla facilisis at vero eros et accumsan et iusto odio dignissim qui blandit praesent luptatum zzril delenit augue duis dolore te feugait nulla facilisi. Duis autem vel eum iriure dolor in hendrerit in vulputate velit esse molestie consequat, vel illum dolore eu feugiat nulla facilisis at vero eros et accumsan et iusto odio dignissim qui blandit praesent luptatum zzril delenit augue duis dolore te feugait nulla facilisi.</p>
  <span class="read-more-link">Read More</span>
  <div class="video" role="img" aria-label="Video still of a remodeled room with a doorway">
    <svg class="play" width="42" height="42" viewBox="0 0 42 42"><circle cx="21" cy="21" r="21" fill="#f26b0f"/><path d="M16 12l14 9-14 9z" fill="#fff"/></svg>
  </div>
</section>

<section class="services">
  <div class="services-photo" role="img" aria-label="Darkened photo of a kitchen interior"></div>
  <div class="services-inner">
    <h2 class="section-heading">Custom Home <span class="accent">Remodeling</span></h2>
    <div class="tagline">You dream it. We build it.</div>

    <div class="service" style="left:99px">
      <div class="service-frame">
        <span class="corner tl"></span><span class="corner tr"></span><span class="corner bl"></span><span class="corner br"></span>
        <div class="service-image" role="img" aria-label="Photo of a remodeled kitchen with wood cabinets" style="background:linear-gradient(180deg,#c9b79a 0%,#8f6a44 55%,#5a3c22 100%)"></div>
      </div>
      <h3 class="service-title">Kitchen Remodeling</h3>
      <p class="service-text">Lorem ipsum dolor sit amet, consectetuer adipiscing elit, sed diam nonummy nibh euismod tincidunt ut laoreet hendrerit in vulputate velit.</p>
      <div class="service-more">Read More</div>
    </div>

    <div class="service" style="left:446px">
      <div class="service-frame">
        <span class="corner tl"></span><span class="corner tr"></span><span class="corner bl"></span><span class="corner br"></span>
        <div class="service-image" role="img" aria-label="Photo of a remodeled bathroom with warm stone tiles" style="background:linear-gradient(180deg,#b0722e 0%,#7a4a1c 55%,#3e2812 100%)"></div>
      </div>
      <h3 class="service-title">Bathroom Remodels</h3>
      <p class="service-text">Lorem ipsum dolor sit amet, consectetuer adipiscing elit, sed diam nonummy nibh euismod tincidunt ut laoreet hendrerit in vulputate velit.</p>
      <div class="service-more">Read More</div>
    </div>

    <div class="service" style="left:793px">
      <div class="service-frame">
        <span class="corner tl"></span><span class="corner tr"></span><span class="corner bl"></span><span class="corner br"></span>
        <div class="service-image" role="img" aria-label="Photo of a house addition with a deck at dusk" style="background:linear-gradient(180deg,#4f6f95 0%,#a8a7a0 55%,#6b5d4a 100%)"></div>
      </div>
      <h3 class="service-title">Home Additions</h3>
      <p class="service-text">Lorem ipsum dolor sit amet, consectetuer adipiscing elit, sed diam nonummy nibh euismod tincidunt ut laoreet hendrerit in vulputate velit.</p>
      <div class="service-more">Read More</div>
    </div>

    <span class="btn-light">Learn more about our home remodeling services</span>
  </div>
</section>

<section class="blog">
  <h2 class="section-heading">Latest from <span class="accent">The Blog</span></h2>

  <article class="post" style="left:98px">
    <div class="post-image" role="img" aria-label="Photo of a bright kitchen overlooking a city view" style="background:linear-gradient(180deg,#9bb0c4 0%,#c7b08a 55%,#7a5a36 100%)"></div>
    <h3 class="post-title">Consectetuer Adipiscin</h3>
    <div class="post-meta">
      <span><svg width="10" height="10" viewBox="0 0 10 10"><circle cx="5" cy="3" r="2.4" fill="#999"/><path d="M0 10c0-3 2-4.5 5-4.5S10 7 10 10z" fill="#999"/></svg>Admin</span>
      <span><svg width="10" height="10" viewBox="0 0 10 10"><rect x="0" y="1.5" width="10" height="8.5" fill="#999"/><rect x="1" y="4" width="8" height="5" fill="#fff"/></svg>May16, 2016</span>
    </div>
    <p class="post-text">Lorem ipsum dolor sit amet, consectetuer adipiscin elit, sed diam nonummy nibh euismod tincidunt ut la dolore magna aliquam erat volutpat.</p>
  </article>

  <article class="post" style="left:440px">
    <div class="post-image" role="img" aria-label="Photo of a bathroom vanity with blue and white wall tiles" style="background:linear-gradient(180deg,#5b6478 0%,#bfc2c8 60%,#8a8c90 100%)"></div>
    <h3 class="post-title">Remodel Inspiration</h3>
    <div class="post-meta">
      <span><svg width="10" height="10" viewBox="0 0 10 10"><circle cx="5" cy="3" r="2.4" fill="#999"/><path d="M0 10c0-3 2-4.5 5-4.5S10 7 10 10z" fill="#999"/></svg>Admin</span>
      <span><svg width="10" height="10" viewBox="0 0 10 10"><rect x="0" y="1.5" width="10" height="8.5" fill="#999"/><rect x="1" y="4" width="8" height="5" fill="#fff"/></svg>May16, 2016</span>
    </div>
    <p class="post-text">Lorem ipsum dolor sit amet, consectetuer adipiscin elit, sed diam nonummy nibh euismod tincidunt ut la dolore magna aliquam erat volutpat.</p>
  </article>

  <article class="post" style="left:782px">
    <div class="post-image" role="img" aria-label="Photo of a bedroom with a wooden bed in an arched alcove" style="background:linear-gradient(180deg,#d8c9a8 0%,#b49a70 55%,#6e4e30 100%)"></div>
    <h3 class="post-title">Construction Company</h3>
    <div class="post-meta">
      <span><svg width="10" height="10" viewBox="0 0 10 10"><circle cx="5" cy="3" r="2.4" fill="#999"/><path d="M0 10c0-3 2-4.5 5-4.5S10 7 10 10z" fill="#999"/></svg>Admin</span>
      <span><svg width="10" height="10" viewBox="0 0 10 10"><rect x="0" y="1.5" width="10" height="8.5" fill="#999"/><rect x="1" y="4" width="8" height="5" fill="#fff"/></svg>May16, 2016</span>
    </div>
    <p class="post-text">Lorem ipsum dolor sit amet, consectetuer adipiscin elit, sed diam nonummy nibh euismod tincidunt ut la dolore magna aliquam erat volutpat.</p>
  </article>
</section>

<section class="testimonial">
  <svg class="quote-icon" width="44" height="44" viewBox="0 0 44 44"><circle cx="22" cy="22" r="20" fill="none" stroke="#fff" stroke-width="2"/><circle cx="17" cy="23" r="3.6" fill="#fff"/><circle cx="27" cy="23" r="3.6" fill="#fff"/><path d="M13.6 23c0-3 1.5-5 4-6M23.6 23c0-3 1.5-5 4-6" fill="none" stroke="#fff" stroke-width="2"/></svg>
  <p class="quote-text">Sed diam nonummy nibh euismod tincidunt ut laoreet dolore magna aliquam erat volutpat. Ut wisi enim ad minim veniam, quis nostrud exerci tation ullamcorper suscipit lobortis nisl ut aliquip ex ea commodo consequat. Duis autem vel eum iriure dolor in hendrerit in vulputate velit esse molestie consequat, vel illum dolore eu feugiat</p>
  <div class="quote-name">Martin<br>Company Name</div>
</section>

<footer class="site-footer">
  <div class="contacts">
    <div class="contact" style="left:0;top:0">
      <span class="icon-ring"><svg width="18" height="18" viewBox="0 0 18 18"><path d="M17 1L1 8l7 2 2 7z" fill="#fff"/></svg></span>
      <span>Suite 4 Harbor Court,<br>18 Linden Avenue, Redwood Point 94061</span>
    </div>
    <div class="contact" style="left:342px;top:0;margin-top:0;height:46px">
      <span class="icon-ring"><svg width="18" height="14" viewBox="0 0 18 14"><rect width="18" height="14" rx="1" fill="#fff"/><path d="M1 1l8 7 8-7" fill="none" stroke="#363636" stroke-width="1.6"/></svg></span>
      <span>hello@quenbrickhall.com</span>
    </div>
    <div class="contact" style="left:630px;top:0;height:46px">
      <span class="icon-ring"><svg width="16" height="16" viewBox="0 0 16 16"><path d="M3 1c1-.8 2-.5 2.5.4l1.2 2.1c.4.8.2 1.6-.5 2l-.7.5c.8 1.8 2 3.1 3.8 3.9l.5-.7c.5-.7 1.4-.8 2.1-.4l2 1.2c1 .6 1.1 1.7.3 2.5-1.6 1.6-3.9 1.6-6.2 0C5.2 11.1 3 8.8 2 6 1.3 4 1.5 2.3 3 1z" fill="#fff"/></svg></span>
      <span>415.555.0148</span>
    </div>
    <div class="contact" style="left:854px;top:0;height:46px">
      <span class="icon-ring"><svg width="18" height="16" viewBox="0 0 18 16"><rect x="4" y="0" width="10" height="4" fill="#fff"/><rect x="0" y="5" width="18" height="7" rx="1" fill="#fff"/><rect x="4" y="10" width="10" height="6" fill="#fff" stroke="#363636" stroke-width="1"/></svg></span>
      <span>415.555.0148</span>
    </div>
  </div>

  <div class="newsletter">
    <h2 class="section-heading">Sign up for <span class="accent">Our Newsletter</span></h2>
    <p>Lorem ipsum dolor sit amet, consectetuer adipiscing elit, sed diam nonummy nibh euismod tincidunt ut laoreet dolore magna aliquam erat volutpat. Ut wisi enim ad minim veniam, quis nostrud exerci tation ullamcorper suscipit lobortis nisl ut aliquip ex ea commodo consequat.</p>
  </div>
  <div class="subscribe">
    <div class="subscribe-field">Subject</div>
    <div class="subscribe-btn">Subscribe</div>
  </div>
</footer>

<footer class="base-bar">
  <nav class="base-nav"><span class="current">Home</span><span>About</span><span>Services</span><span>Gallery</span><span>Contact Us</span></nav>
  <div class="copyright">© All Rights Reserved 2016</div>
</footer>

</body>
</html>
```